Software company WebSite Design (enterprise level SW, Mobile apps, HW prototypes)

We need design for our new webpages. We got new logo and new business cards and we need webdesign which will be match with those two.
We are dealing with corporate level software development - enterprise level portals, development of optimalization SW, route planning optimalizations. For a few months we are developing mobile applications for companies.
IMPORTANT is to express the cutting edge technological company.

Target Market(s)

IT company customers

Industry/Entity Type

Business

Number of Pages Required

2 page

Requirements
Must have
• Project needs to have landing page and product detail page. Design needs to be created including full font and example images as there would be a real webpage. Design should be clean, modern and expressing hi-tech level of the company.
• Example of well designer web pages - www.quorvelt.com, www.brandissa.com - We like the font formatting and font designs (colors, placing, etc - its professional).
• Attached image contains screenshot from old web landing page. It contains basic sections of our business (Simulation Tools, Enterprise Intranet Systems, Hi-tech web presentations, Supporting Enterprise services - Optimalization and logistics monitoring)

```html
<!DOCTYPE html>
<html lang="en">
<head>
<meta charset="utf-8">
<title>Kvaro Solutions</title>
<link href="https://fonts.googleapis.com/css2?family=Source+Sans+3:wght@400;600;700&family=Open+Sans+Condensed:wght@700&display=swap" rel="stylesheet">
<style>
:root{
  --page:#ebebeb;
  --white:#ffffff;
  --blue:#0a8fd6;
  --blue-dark:#0672b0;
  --badge:#d9e9f3;
  --ink:#4d4d4d;
  --text:#666666;
  --muted:#8a8a8a;
  --grey-btn:#9a9a9a;
  --footer:#2d2d2d;
  --line:#d4d4d4;
}
*{box-sizing:border-box;margin:0;padding:0}
html,body{width:1200px;height:2344px;overflow:hidden}
body{background:var(--page);font-family:"Source Sans 3",Arial,sans-serif;color:var(--text);position:relative}
.site{position:absolute;left:16px;top:0;width:1168px;background:var(--white);box-shadow:0 2px 8px rgba(0,0,0,.12)}
/* header */
.header{position:relative;height:153px;background:linear-gradient(#f7f7f7,#ececec)}
.brand{position:absolute;left:30px;top:52px;display:flex;align-items:center;gap:14px}
.brand-mark{width:40px;height:40px;background:var(--blue)}
.brand-name{font-weight:700;font-size:44px;color:#3c3c3c;letter-spacing:1px;line-height:1}
.brand-name small{display:block;font-size:14px;letter-spacing:6px;font-weight:600;margin-top:2px}
.contact-top{position:absolute;top:24px;display:flex;align-items:center;gap:12px}
.contact-top .ico{width:40px;height:40px;border-radius:50%;border:2px solid #8a8a8a;display:flex;align-items:center;justify-content:center}
.contact-top .lbl{font-size:13px;font-weight:700;color:var(--muted);line-height:1}
.contact-top .val{font-size:24px;color:#4a4a4a;font-weight:600;line-height:1.1}
.c-phone{left:648px}
.c-mail{left:918px}
.menu{position:absolute;left:470px;top:90px;width:678px;height:45px}
.menu svg{position:absolute;inset:0}
.menu ul{position:absolute;inset:0;display:flex;list-style:none;padding-left:110px;gap:58px;align-items:center}
.menu li{font-size:16px;font-weight:600;color:#555;position:relative}
.menu li.active{color:var(--blue)}
.menu li.active::before{content:"";position:absolute;left:50%;top:-12px;margin-left:-7px;border:7px solid transparent;border-top-color:var(--blue)}
.servicebar{height:41px;background:var(--blue);display:flex;justify-content:space-around;align-items:center;padding:0 60px;border-top:1px solid #6bc0ee}
.servicebar a{color:var(--white);font-family:"Open Sans Condensed","Arial Narrow",sans-serif;font-weight:700;font-size:15px;text-decoration:none}
/* slider */
.slider{position:relative;height:459px;background:radial-gradient(ellipse at 48% 50%,#1a8ec9 0%,#16547a 30%,#3d4651 60%,#8c9197 100%)}
.slider .arrow{position:absolute;top:206px;width:50px;height:50px;background:var(--blue);display:flex;align-items:center;justify-content:center}
.arrow.prev{left:0}.arrow.next{right:0}
.dots{position:absolute;left:572px;bottom:12px;display:flex;gap:6px}
.dots span{width:11px;height:11px;border-radius:50%;border:1px solid #fff;background:rgba(255,255,255,.3)}
.dots span:first-child{background:#fff}
/* sections */
.section-title{text-align:center;font-size:25px;font-weight:700;color:var(--ink);letter-spacing:.3px}
.divider{position:relative;height:20px;margin:10px 59px 0;border-top:1px solid var(--line)}
.divider::after{content:"";position:absolute;left:50%;top:-9px;margin-left:-9px;width:18px;height:18px;border-radius:50%;background:var(--blue);border:3px solid var(--white)}
.about{height:386px;padding-top:56px}
.about p{width:1020px;margin:30px auto 0;text-align:center;font-size:16.5px;line-height:22px;color:var(--text)}
.btn-more{display:flex;align-items:center;justify-content:space-between;width:160px;height:33px;margin:35px auto 0;padding:0 8px 0 14px;background:linear-gradient(90deg,var(--blue) 70%,var(--blue-dark) 70%);border-radius:3px;color:#fff;font-weight:700;font-size:14px}
.btn-more i{width:20px;height:20px;border-radius:50%;background:#2a2a2a;display:flex;align-items:center;justify-content:center}
.services{position:relative;height:489px;background:linear-gradient(135deg,#f2f2f2,#e6e6e6 50%,#efefef)}
.service{position:absolute;width:380px;height:160px}
.service .badge{position:absolute;left:14px;top:14px;width:104px;height:104px;border-radius:50%;background:var(--badge)}
.service h3{position:absolute;left:150px;top:0;font-size:17px;font-weight:700;color:var(--ink);white-space:nowrap}
.service p{position:absolute;left:150px;top:22px;width:215px;font-size:16px;line-height:22px;color:var(--text)}
.service .btn{position:absolute;left:150px;top:122px;width:160px;height:32px;background:var(--grey-btn);border-radius:3px;color:#fff;font-weight:700;font-size:14px;display:flex;align-items:center;justify-content:center}
.blog{height:535px;padding-top:52px}
.cards{position:relative;margin-top:28px;height:330px}
.card{position:absolute;top:0;width:266px;height:328px;background:linear-gradient(90deg,#e4e4e4,#fafafa 50%,#e4e4e4);border:1px solid #ddd;box-shadow:0 1px 4px rgba(0,0,0,.15)}
.card .photo{margin:4px;height:181px}
.card h4{margin:14px 0 0 14px;font-size:15px;font-weight:700;color:#333}
.card p{margin:2px 14px 0;font-size:14.5px;line-height:18px;color:#333}
.card .btn{position:absolute;left:43px;bottom:20px;width:180px;height:44px;background:var(--blue);border-radius:3px;color:#fff;font-weight:600;font-size:16px;display:flex;align-items:center;justify-content:center}
/* footer */
.footer{position:relative;height:226px;background:var(--footer);overflow:hidden}
.footer .panel{position:absolute;inset:0}
.fcol{position:absolute;top:40px;color:#fff}
.fcol h5{font-size:16px;font-weight:700;margin-bottom:10px}
.fcol li{list-style:none;font-size:13.5px;font-weight:700;line-height:21px}
.fcol .row{display:flex;gap:12px;font-size:13.5px;font-weight:700;line-height:18px;margin-bottom:16px}
.f-brand{position:absolute;left:850px;top:74px;display:flex;align-items:center;gap:14px}
.socials{position:absolute;left:888px;top:155px;display:flex;gap:6px}
.socials span{width:30px;height:30px;border-radius:50%;background:#9a9a9a}
.copyright{height:39px;display:flex;align-items:center;justify-content:center;font-size:11.5px;font-weight:700;color:#333}
</style>
</head>
<body>
<div class="site">
  <header class="header">
    <div class="brand">
      <span class="brand-mark"></span>
      <span class="brand-name">KVARO<small>SOLUTIONS</small></span>
    </div>
    <div class="contact-top c-phone">
      <span class="ico"><svg width="20" height="20" viewBox="0 0 24 24"><path d="M6.6 10.8a15 15 0 0 0 6.6 6.6l2.2-2.2c.3-.3.7-.4 1-.2 1.1.4 2.3.6 3.6.6.6 0 1 .4 1 1V20c0 .6-.4 1-1 1A17 17 0 0 1 3 4c0-.6.4-1 1-1h3.5c.6 0 1 .4 1 1 0 1.3.2 2.5.6 3.6.1.3 0 .7-.2 1z" fill="#8a8a8a"/></svg></span>
      <div><div class="lbl">FOR MORE INFORMATION</div><div class="val">555 210 384</div></div>
    </div>
    <div class="contact-top c-mail">
      <span class="ico"><svg width="20" height="16" viewBox="0 0 20 16"><rect x="1" y="1" width="18" height="14" rx="1" fill="none" stroke="#8a8a8a" stroke-width="2"/><path d="M1 2l9 7 9-7" fill="none" stroke="#8a8a8a" stroke-width="2"/></svg></span>
      <div class="val">mnovak@kvaro.cz</div>
    </div>
    <nav class="menu">
      <svg width="678" height="45" viewBox="0 0 678 45"><polygon points="40,0 678,0 640,45 0,45" fill="#f4f4f4"/><polygon points="620,0 678,0 640,45 590,45" fill="#dcdcdc"/></svg>
      <ul><li class="active">HOME</li><li>ABOUT US</li><li>BLOG</li><li>CONTACT US</li></ul>
    </nav>
  </header>
  <nav class="servicebar">
    <a>SOFTWARE DEVELOPMENT</a><a>ENTERPRISE LEVEL PORTALS</a><a>SOFTWARE OPTIMIZATION</a><a>ROUTE PLANNING OPTIMIZATION</a><a>MOBILE APPLICATIONS</a>
  </nav>
  <section class="slider" role="img" aria-label="Hero banner: glowing globe surrounded by a network of connected business icons, charts and a tablet">
    <span class="arrow prev"><svg width="14" height="20" viewBox="0 0 14 20"><path d="M11 2L3 10l8 8" fill="none" stroke="#fff" stroke-width="3"/></svg></span>
    <span class="arrow next"><svg width="14" height="20" viewBox="0 0 14 20"><path d="M3 2l8 8-8 8" fill="none" stroke="#fff" stroke-width="3"/></svg></span>
    <div class="dots"><span></span><span></span><span></span></div>
  </section>
  <section class="about">
    <h2 class="section-title">ABOUT KVARO SOLUTIONS</h2>
    <div class="divider"></div>
    <p>Lorem ipsum dolor sit amet, consectetuer adipiscing elit, sed diam nonummy nibh euismod tincidunt ut laoreet dolore magna aliquam erat volutpat. Ut wisi enim ad minim veniam, quis nostrud exerci tation ullamcorper suscipit lobortis nisl ut aliquip ex ea commodo consequat. Duis autem vel eum iriure dolor in hendrerit in vulputate velit esse molestie consequat, vel illum dolore eu feugiat nulla facilisis at vero eros et accumsan et iusto odio dignissim qui blandit praesent luptatum zzril delenit augue duis dolore te feugait nulla facilisi. Nam liber tempor cum soluta nobis eleifend option congue nihil imperdiet doming id quod mazim placerat facer possim assum.</p>
    <div class="btn-more">LEARN MORE<i><svg width="10" height="10" viewBox="0 0 10 10"><path d="M1 5h7M5 2l3 3-3 3" fill="none" stroke="#fff" stroke-width="1.6"/></svg></i></div>
  </section>
  <section class="services">
    <div class="service" style="left:12px;top:60px"><span class="badge"></span><h3>SOFTWARE DEVELOPMENT</h3><p>Lorem ipsum dolor sit amet, consectetuer adipiscing elit, sed diam nonummy nibh euis mod tincidunt ut laoreet.</p><span class="btn">LEARN MORE</span></div>
    <div class="service" style="left:402px;top:60px"><span class="badge"></span><h3>ENTERPRISE LEVEL PORTAL</h3><p>Lorem ipsum dolor sit amet, consectetuer adipiscing elit, sed diam nonummy nibh euis mod tincidunt ut laoreet.</p><span class="btn">LEARN MORE</span></div>
    <div class="service" style="left:792px;top:60px"><span class="badge"></span><h3>SOFTWARE OPTIMIZATION</h3><p>Lorem ipsum dolor sit amet, consectetuer adipiscing elit, sed diam nonummy nibh euis mod tincidunt ut laoreet.</p><span class="btn">LEARN MORE</span></div>
    <div class="service" style="left:213px;top:270px"><span class="badge"></span><h3>ROUTE PLANNING</h3><p>Lorem ipsum dolor sit amet, consectetuer adipiscing elit, sed diam nonummy nibh euis mod tincidunt ut laoreet.</p><span class="btn">LEARN MORE</span></div>
    <div class="service" style="left:603px;top:270px"><span class="badge"></span><h3>MOBILE APPLICATIONS</h3><p>Lorem ipsum dolor sit amet, consectetuer adipiscing elit, sed diam nonummy nibh euis mod tincidunt ut laoreet.</p><span class="btn">LEARN MORE</span></div>
  </section>
  <section class="blog">
    <h2 class="section-title">LATEST FROM THE BLOG</h2>
    <div class="divider"></div>
    <div class="cards">
      <article class="card" style="left:31px"><div class="photo" role="img" aria-label="Photo of colleagues talking around a laptop in an office" style="background:linear-gradient(135deg,#dfe3e6,#8e9aa3 60%,#c9cfd3)"></div><h4>News #1</h4><p>Lorem ipsum dolor sit amet, consec tetuer adipiscing elit, sed diam.</p><span class="btn">READ MORE</span></article>
      <article class="card" style="left:311px"><div class="photo" role="img" aria-label="Photo of a glowing puzzle piece on a teal puzzle surface" style="background:radial-gradient(circle at 55% 45%,#cfe6ea,#3f7f8c 45%,#17393f)"></div><h4>News #2</h4><p>Lorem ipsum dolor sit amet, consec tetuer adipiscing elit, sed diam.</p><span class="btn">READ MORE</span></article>
      <article class="card" style="left:590px"><div class="photo" role="img" aria-label="Photo of a hand touching floating digital icons" style="background:radial-gradient(circle at 50% 50%,#5a8ec4,#1c3560 55%,#0c1730)"></div><h4>News #3</h4><p>Lorem ipsum dolor sit amet, consec tetuer adipiscing elit, sed diam.</p><span class="btn">READ MORE</span></article>
      <article class="card" style="left:870px"><div class="photo" role="img" aria-label="Photo of blurred people walking through a bright glass office lobby" style="background:linear-gradient(90deg,#8fb7c2,#d9ecef 45%,#5f8f9c)"></div><h4>News #4</h4><p>Lorem ipsum dolor sit amet, consec tetuer adipiscing elit, sed diam.</p><span class="btn">READ MORE</span></article>
    </div>
  </section>
  <footer class="footer">
    <svg class="panel" width="1168" height="226" viewBox="0 0 1168 226"><polygon points="840,0 1168,0 1168,226 672,226" fill="#eeeeee"/></svg>
    <div class="fcol" style="left:78px"><h5>QUICK LINKS</h5><ul><li>HOME</li><li>ABOUT US</li><li>BLOG</li><li>CONTACT</li></ul></div>
    <div class="fcol" style="left:265px"><h5>SERVICES</h5><ul><li>SOFTWARE DEVELOPMENT</li><li>ENTERPRISE LEVEL PORTAL</li><li>SOFTWARE OPTIMIZATION</li><li>ROUTE PLANNING</li><li>MOBILE APPLICATIONS</li></ul></div>
    <div class="fcol" style="left:538px"><h5>CONTACT</h5>
      <div class="row"><svg width="12" height="16" viewBox="0 0 12 16"><path d="M6 0a6 6 0 0 1 6 6c0 4-6 10-6 10S0 10 0 6a6 6 0 0 1 6-6z" fill="#fff"/><circle cx="6" cy="6" r="2.2" fill="#2d2d2d"/></svg><span>Lipová 412<br>33201 Brezno</span></div>
      <div class="row"><svg width="16" height="14" viewBox="0 0 16 14"><path d="M1 4c0-2 3-3 7-3s7 1 7 3v2h-4V4H5v2H1zM3 7h10l1 6H2z" fill="#fff"/></svg><span>555 210 384</span></div>
      <div class="row"><svg width="16" height="12" viewBox="0 0 16 12"><rect x="1" y="1" width="14" height="10" fill="none" stroke="#fff" stroke-width="1.5"/><path d="M1 1l7 6 7-6" fill="none" stroke="#fff" stroke-width="1.5"/></svg><span>mnovak@kvaro.cz</span></div>
    </div>
    <div class="f-brand"><span class="brand-mark"></span><span class="brand-name">KVARO<small>SOLUTIONS</small></span></div>
    <div class="socials"><span></span><span></span><span></span><span></span><span></span></div>
  </footer>
  <div class="copyright">© 2016 KVARO SOLUTIONS. ALL RIGHTS RESERVED.</div>
</div>
</body>
</html>
```